Label design for an exciting new Vodka brand

We need a label design for a dynamic new Vodka brand called 'Pale lantern Vodka'. It is a crisp and versatile liquid with a clean and smooth finish. It should appeal to 21-39 year olds, with a slight female skew. Colours, fonts and styles should be modern and relatively neutral - take inspiration from the brand pictures attached.

Target Market(s)

21-39 year olds, both male and female, but with a slight female skew

```html
<!DOCTYPE html>
<html lang="en">
<head>
<meta charset="utf-8">
<title>Pale Lantern Vodka – Label</title>
<link rel="stylesheet" href="https://fonts.googleapis.com/css2?family=Quattrocento:wght@400&display=swap">
<style>
  :root {
    --page: #ffffff;
    --label-paper: #e6e7e6;
    --band: #15161c;
    --ink: #2b2b2b;
    --ink-soft: #4a4a4a;
    --rule: #8a8a8a;
    --gold: #c9a24c;
    --gold-light: #e6cf93;
    --grain: #d9c9a6;
  }
  html, body {
    margin: 0;
    padding: 0;
    width: 1200px;
    height: 2250px;
    overflow: hidden;
    background: var(--page);
  }
  .canvas {
    position: relative;
    width: 1200px;
    height: 2250px;
  }
  .label {
    position: absolute;
    left: 60px;
    top: 402px;
    width: 1080px;
    height: 1445px;
    background: var(--label-paper);
    overflow: hidden;
  }
  .label__band {
    position: absolute;
    left: 0;
    width: 100%;
    height: 36px;
    background: var(--band);
  }
  .label__band--top { top: 0; }
  .label__band--bottom { bottom: 0; }
  .label__grain {
    position: absolute;
    left: 0;
    top: 36px;
    width: 620px;
    height: 1373px;
    background:
      radial-gradient(ellipse 55% 45% at 30% 40%, rgba(217, 201, 166, 0.55), rgba(217, 201, 166, 0) 70%),
      linear-gradient(90deg, rgba(217, 201, 166, 0.45), rgba(217, 201, 166, 0) 100%);
  }
  .label__text {
    position: absolute;
    left: 0;
    width: 100%;
    margin: 0;
    text-align: center;
    font-family: "Quattrocento", serif;
    font-weight: 400;
  }
  .wordmark {
    top: 360px;
    font-size: 104px;
    line-height: 136px;
    letter-spacing: 6px;
    color: var(--ink);
  }
  .tagline {
    top: 1036px;
    font-size: 27px;
    line-height: 38px;
    color: var(--ink-soft);
  }
  .tagline-rule {
    position: absolute;
    left: 298px;
    width: 410px;
    height: 2px;
    background: linear-gradient(90deg, rgba(138,138,138,0), var(--rule) 15%, var(--rule) 85%, rgba(138,138,138,0));
  }
  .tagline-rule--above { top: 1022px; }
  .tagline-rule--below { top: 1127px; }
  .volume {
    top: 1282px;
    font-size: 30px;
    line-height: 1;
    letter-spacing: 2px;
    color: var(--ink);
  }
  .gold-rules {
    position: absolute;
    left: 0;
    top: 1336px;
    width: 1080px;
    height: 30px;
  }
</style>
</head>
<body>
<main class="canvas">
  <section class="label" aria-label="Pale Lantern Vodka bottle label">
    <div class="label__band label__band--top"></div>
    <div class="label__grain" role="img" aria-label="Fine gold wood-grain line pattern"></div>

    <h1 class="label__text wordmark">PALE LANTERN<br>VODKA</h1>

    <div class="tagline-rule tagline-rule--above"></div>
    <p class="label__text tagline">It is a crisp and versatile<br>liquid with a clean and smooth finish</p>
    <div class="tagline-rule tagline-rule--below"></div>

    <p class="label__text volume">15.9 FL.OZ. ( 500ML)</p>

    <svg class="gold-rules" viewBox="0 0 1080 30" aria-hidden="true">
      <line x1="0" y1="7" x2="517" y2="7" stroke="var(--gold)" stroke-width="3"/>
      <line x1="0" y1="22" x2="517" y2="22" stroke="var(--gold-light)" stroke-width="3"/>
      <line x1="570" y1="7" x2="1080" y2="7" stroke="var(--gold)" stroke-width="3"/>
      <line x1="570" y1="22" x2="1080" y2="22" stroke="var(--gold-light)" stroke-width="3"/>
    </svg>

    <div class="label__band label__band--bottom"></div>
  </section>
</main>
</body>
</html>
```